Mixed Martial Arts gym that is known for high quality athletes, students and training

We need a business card designed that is unique and stands out. Something that is not so dark and boring but looks 'energetic' to those that are given it. The customers that would receive this card would be looking to sign up for martial arts or fitness training and this card is used for corporate sponsorships and networking as well.

Marcus Penhale-Orwin
0457302194 or 0469150836
Suite 3, 214 Quarrion Road. Kestrelvale NSW 2931
marcus@ironpeakcombatcentre.com.au
www.ironpeakcombatcentre.com

```html
<!DOCTYPE html>
<html lang="en">
<head>
<meta charset="utf-8">
<title>Iron Peak Combat Centre – Business Card</title>
<link rel="stylesheet" href="https://fonts.googleapis.com/css2?family=Open+Sans:wght@700&family=Barlow+Semi+Condensed:wght@400&display=swap">
<style>
  :root {
    --page-bg: #ebebeb;
    --card-light: #f4f4f4;
    --card-mid: #d6d6d6;
    --card-edge: #c2c2c2;
    --brand-orange: #e8962a;
    --ink: #1b1b1b;
    --ink-soft: #2b2b2b;
  }
  * { box-sizing: border-box; margin: 0; padding: 0; }
  html, body {
    width: 1200px;
    height: 1017px;
    overflow: hidden;
    background: var(--page-bg);
  }
  .sheet {
    width: 1200px;
    height: 1017px;
    display: flex;
    flex-direction: column;
    align-items: center;
    justify-content: center;
    gap: 44px;
  }
  .card {
    position: relative;
    width: 740px;
    height: 450px;
    border-radius: 4px;
    overflow: hidden;
    background: radial-gradient(ellipse 70% 75% at 50% 50%, var(--card-light) 0%, #e4e4e4 45%, var(--card-mid) 80%, var(--card-edge) 100%);
    box-shadow: 0 6px 18px rgba(0,0,0,0.12), 0 1px 3px rgba(0,0,0,0.12);
  }

  /* Front face */
  .card-front .brand-lockup {
    position: absolute;
    left: 50%;
    top: 50%;
    transform: translate(-50%, -50%);
    display: flex;
    align-items: center;
    gap: 18px;
  }
  .brand-mark {
    width: 34px;
    height: 34px;
    background: var(--ink);
  }
  .brand-name {
    font-family: "Open Sans", sans-serif;
    font-weight: 700;
    color: var(--brand-orange);
    text-transform: uppercase;
    line-height: 1.05;
    white-space: nowrap;
  }
  .card-front .brand-name {
    font-size: 44px;
    letter-spacing: 0.5px;
  }

  /* Back face */
  .holder-name {
    position: absolute;
    right: 48px;
    top: 46px;
    font-family: "Open Sans", sans-serif;
    font-weight: 700;
    font-size: 28px;
    color: var(--ink);
    white-space: nowrap;
  }
  .contact-tab {
    position: absolute;
    left: 0;
    top: 108px;
    width: 50px;
    height: 140px;
    background: var(--brand-orange);
    border-radius: 0 8px 8px 0;
    display: flex;
    flex-direction: column;
    align-items: center;
    justify-content: center;
    gap: 11px;
  }
  .contact-tab svg {
    width: 16px;
    height: 16px;
    fill: var(--ink);
  }
  .contact-details {
    position: absolute;
    left: 74px;
    top: 124px;
    font-family: "Barlow Semi Condensed", sans-serif;
    font-weight: 400;
    font-size: 19px;
    line-height: 27px;
    color: var(--ink-soft);
    list-style: none;
    white-space: nowrap;
  }
  .card-back .brand-lockup {
    position: absolute;
    right: 48px;
    bottom: 52px;
    display: flex;
    align-items: center;
    gap: 10px;
  }
  .card-back .brand-mark {
    width: 18px;
    height: 18px;
  }
  .card-back .brand-name {
    font-size: 18px;
  }
</style>
</head>
<body>
<main class="sheet">

  <section class="card card-front" aria-label="Business card front">
    <div class="brand-lockup">
      <span class="brand-mark" aria-hidden="true"></span>
      <span class="brand-name">Iron Peak<br>Combat Centre</span>
    </div>
  </section>

  <section class="card card-back" aria-label="Business card back">
    <p class="holder-name">Marcus Penhale-Orwin</p>

    <div class="contact-tab" aria-hidden="true">
      <svg viewBox="0 0 16 16"><path d="M8 0a5.5 5.5 0 0 0-5.5 5.5C2.5 9.6 8 16 8 16s5.5-6.4 5.5-10.5A5.5 5.5 0 0 0 8 0zm0 7.8a2.3 2.3 0 1 1 0-4.6 2.3 2.3 0 0 1 0 4.6z"/></svg>
      <svg viewBox="0 0 16 16"><path d="M3.6 1.2 5.8 3.4c.4.4.4 1 0 1.4L4.7 5.9a9.6 9.6 0 0 0 5.4 5.4l1.1-1.1c.4-.4 1-.4 1.4 0l2.2 2.2c.4.4.4 1 0 1.4l-1.2 1.2c-.7.7-1.800.9-2.7.5A15.6 15.6 0 0 1 1.5 6.1C1.1 5.2 1.3 4.1 2 3.4l1.6-2.2z"/></svg>
      <svg viewBox="0 0 16 16"><path d="M1 3h14v1.2L8 9 1 4.2V3zm0 2.6 7 4.8 7-4.8V13H1V5.6z"/></svg>
      <svg viewBox="0 0 16 16"><path d="M8 0a8 8 0 1 0 0 16A8 8 0 0 0 8 0zm5.9 7.3h-2.6a12 12 0 0 0-1-4.9 6.1 6.1 0 0 1 3.6 4.9zM8 1.8c.7.9 1.4 2.8 1.6 5.5H6.4C6.6 4.6 7.3 2.7 8 1.8zM5.7 2.4a12 12 0 0 0-1 4.9H2.1a6.1 6.1 0 0 1 3.6-4.9zM2.1 8.7h2.6c.1 1.9.5 3.6 1 4.9a6.1 6.1 0 0 1-3.6-4.9zM8 14.2c-.7-.9-1.4-2.8-1.6-5.5h3.2c-.2 2.7-.9 4.6-1.6 5.5zm2.3-.6c.5-1.3.9-3 1-4.9h2.6a6.1 6.1 0 0 1-3.6 4.9z"/></svg>
    </div>

    <ul class="contact-details">
      <li class="contact-address">Suite 3, 214 Quarrion Road. Kestrelvale NSW 2931</li>
      <li class="contact-phone">045.730.2194 / 046.915.0836</li>
      <li class="contact-email">marcus@ironpeakcombatcentre.com.au</li>
      <li class="contact-web">www.ironpeakcombatcentre.com</li>
    </ul>

    <div class="brand-lockup">
      <span class="brand-mark" aria-hidden="true"></span>
      <span class="brand-name">Iron Peak<br>Combat Centre</span>
    </div>
  </section>

</main>
</body>
</html>
```